New Business Card for chocolate Company

I am looking to have business cards for my Chocolate Company Velvet Hollow Sweets.
I hand make all organic, fair trade, vegan, gluten free, allergy friendly chocolate. We are located in Austin Texas and are very Proud to be a locally made good. I have my logo and new sticker design for our boxes but now I need cards. I was thinking either natural craft or white. But I want to have a bit of funk to the cards so someone will hold onto it for a long time.
The important info is
Dana Pelworth
Owner and Chocolatier
Velvet Hollow Sweets
velvethollowsweetsatx.com
velvethollowsweets@brivomail.com
velvethollowsweets on pixgram
512.373.4816

Velvet Hollow sweets are Vegan ,Gluten free, organic, fair trade, allergy friendly hand made chocolate.

Target Market(s)

We cater to all ages. Our chocolate is on the higher price scale and is a decadent treat. But we make custom molds for any event kids party's to an elegant wedding.

Industry/Entity Type

Business

Requirements
Must have
• Good design logo and some sort of austin vibe.

```html
<!DOCTYPE html>
<html lang="en">
<head>
<meta charset="utf-8">
<title>Velvet Hollow Sweets — Business Card</title>
<link rel="stylesheet" href="https://fonts.googleapis.com/css2?family=Josefin+Sans:wght@400;600&display=swap">
<style>
  :root {
    --backdrop: #e8e5e7;
    --teal: #00656f;
    --white: #ffffff;
    --pattern-tint: #eef6f5;
    --card-shadow: rgba(0, 0, 0, 0.22);
  }
  * { box-sizing: border-box; margin: 0; padding: 0; }
  html, body {
    width: 1200px;
    height: 901px;
    overflow: hidden;
    background: var(--backdrop);
    font-family: "Josefin Sans", sans-serif;
  }
  .stage { position: relative; width: 1200px; height: 901px; }
  .card {
    position: absolute;
    left: 300px;
    width: 597px;
    height: 340px;
    box-shadow: 0 3px 8px var(--card-shadow);
  }
  .card-front { top: 74px; background: var(--teal); color: var(--white); }
  .card-back { top: 467px; background: var(--white); color: var(--teal); }

  .brand-name {
    position: absolute;
    left: 0; right: 0; top: 92px;
    text-align: center;
    font-weight: 600;
    font-size: 40px;
    line-height: 46px;
    letter-spacing: 2px;
    text-transform: uppercase;
  }
  .tagline {
    position: absolute;
    left: 0; right: 0; top: 322px;
    text-align: center;
    font-size: 13px;
    letter-spacing: 0.3px;
    text-transform: uppercase;
  }

  .pattern-field {
    position: absolute;
    inset: 0;
    background: var(--pattern-tint);
  }
  .contact {
    position: absolute;
    left: 0; right: 0;
    text-align: center;
  }
  .contact-name { top: 162px; font-size: 25px; }
  .contact-role { top: 195px; font-size: 12px; }
  .contact-phone { top: 242px; font-size: 17px; font-weight: 600; letter-spacing: 0.5px; }
  .contact-links { top: 265px; font-size: 16px; }
  .contact-links span + span { margin-left: 22px; }
  .contact-social { top: 289px; font-size: 16px; }
</style>
</head>
<body>
<main class="stage">
  <section class="card card-front">
    <h1 class="brand-name">Velvet Hollow<br>Sweets</h1>
    <p class="tagline">Vegan - Gluten Free - Allergy Friendly - Organic - Fair Trade Chocolate</p>
  </section>

  <section class="card card-back">
    <div class="pattern-field" role="img" aria-label="Faint repeating pattern of crossed arrows"></div>
    <p class="contact contact-name">Dana Pelworth</p>
    <p class="contact contact-role">Owner and Chocolatier</p>
    <p class="contact contact-phone">512.373.4816</p>
    <p class="contact contact-links"><span>velvethollowsweetsatx.com</span><span>velvethollowsweets@brivomail.com</span></p>
    <p class="contact contact-social">velvethollowsweets on pixgram</p>
  </section>
</main>
</body>
</html>
```